Fleet Wrap - Wall Partitions Company

We are looking for a vehicle/fleet wrap design for Brightfold Panel Works, a company that sells and installs operable/folding wall partitions for commercial spaces. Our systems are used in offices, schools, hotels, conference centers, and other spaces that need flexible room configurations.

The goal of the wrap is to improve brand visibility and recognition while our vehicles are on the road and at job sites. We want the design to feel modern, professional, architectural, and memorable, while making it immediately clear what our company does.

The design should incorporate imagery, graphics, or architectural elements that communicate movable walls, folding partitions, and/or flexible spaces, along with our company colors (see logo attached). As well as display our logo/name, location, and phone number (obtained from our website - brightfoldpanels.example). We are open to creative concepts, but would prefer something clean and distinctive rather than overly busy.

The vehicle we want wrapped, is a KESTA Voyant 2400 (see link here - https://www.kestavans.example/kesta-voyant/specs.2400-cargo-van-high-roof-159-wb.html)

Key priorities:
- Strong brand visibility from a distance
- Contemporary, architectural look
- Clearly communicate that we sell and install folding/operable wall systems
- Easy-to-read company name and website
- Professional enough for commercial construction and corporate clients

```html
<!DOCTYPE html>
<html lang="en">
<head>
<meta charset="utf-8">
<title>Brightfold Panel Works – Fleet Wrap</title>
<link rel="stylesheet" href="https://fonts.googleapis.com/css2?family=Marcellus&family=Montserrat:wght@500;600&display=swap">
<style>
  :root{
    --bg:#eef0f3;
    --body-white:#fbfbfc;
    --navy:#14284b;
    --accent-blue:#1f7ae0;
    --brand-orange:#f18a12;
    --charcoal:#2f3236;
    --tire:#1f2124;
    --glass:#24282e;
    --photo-light:#d9dcdf;
    --photo-mid:#a9adb1;
    --taillight:#b3121b;
    --ink:#1d2430;
    --label:#ffffff;
  }
  html,body{margin:0;padding:0;width:1200px;height:800px;overflow:hidden;background:var(--bg);}
  .wrap-sheet{display:block;width:1200px;height:800px;}
  .brand-name{font-family:"Marcellus",serif;fill:var(--ink);letter-spacing:1px;}
  .brand-sub{font-family:"Marcellus",serif;fill:var(--ink);letter-spacing:3px;}
  .service-label{font-family:"Montserrat",sans-serif;font-weight:600;font-size:8.5px;fill:var(--label);letter-spacing:.4px;}
  .contact-line{font-family:"Montserrat",sans-serif;font-weight:500;font-size:8px;fill:var(--label);}
  .maker-badge{font-family:"Montserrat",sans-serif;font-weight:600;fill:#c9ccd0;letter-spacing:3px;}
  .icon-line{fill:none;stroke:var(--label);stroke-width:1.3;}
</style>
</head>
<body>
<svg class="wrap-sheet" viewBox="0 0 1200 800" xmlns="http://www.w3.org/2000/svg">
  <defs>
    <linearGradient id="interiorTone" x1="0" y1="0" x2="1" y2="1">
      <stop offset="0" stop-color="#eceef0"/>
      <stop offset=".55" stop-color="#c4c7cb"/>
      <stop offset="1" stop-color="#8e9297"/>
    </linearGradient>
    <clipPath id="sideBody">
      <path d="M95 300 L100 255 Q118 208 190 192 L300 98 Q332 48 400 45 L1110 45 Q1136 48 1138 80 L1145 340 L95 340 Z"/>
    </clipPath>
    <clipPath id="rearBody">
      <path d="M170 418 Q310 406 450 418 Q466 440 468 520 L468 720 L146 720 L148 520 Q150 440 170 418 Z"/>
    </clipPath>
  </defs>

  <!-- ===== Side elevation ===== -->
  <g class="side-view">
    <path d="M95 300 L100 255 Q118 208 190 192 L300 98 Q332 48 400 45 L1110 45 Q1136 48 1138 80 L1145 340 L95 340 Z" fill="var(--body-white)" stroke="#d5d8dc"/>
    <g clip-path="url(#sideBody)">
      <rect class="interior-photo" role="img" aria-label="Photo of an office corridor lined with folding partition walls" x="700" y="45" width="450" height="300" fill="url(#interiorTone)" transform="skewX(0)"/>
      <polygon points="0,0" fill="none"/>
      <polygon points="700,345 915,45 1150,45 1150,345" fill="none"/>
      <polygon points="600,45 700,45 700,345 500,345" fill="var(--body-white)"/>
      <polygon points="650,236 790,47 915,47 760,236" fill="#b9bcc0" opacity=".55"/>
      <polygon points="700,236 760,236 700,330 650,330" fill="var(--body-white)"/>
      <polygon points="310,330 380,236 760,236 705,330" fill="var(--navy)"/>
      <polygon points="700,330 760,236 770,236 714,330" fill="var(--navy)"/>
      <polygon points="700,345 915,45 925,45 711,345" fill="var(--accent-blue)"/>
      <polygon points="760,170 915,45 1000,45 770,175" fill="var(--navy)" opacity=".9"/>
      <rect x="860" y="272" width="290" height="70" fill="var(--charcoal)"/>
    </g>
    <!-- cab glass and details -->
    <path d="M255 200 L322 110 Q335 100 360 100 L372 102 L368 205 Z" fill="var(--glass)"/>
    <rect x="355" y="200" width="18" height="28" rx="4" fill="var(--charcoal)"/>
    <rect x="232" y="160" width="16" height="48" rx="5" fill="var(--charcoal)"/>
    <path d="M95 270 L100 330 L180 335 L175 270 Z" fill="var(--charcoal)"/>
    <text class="maker-badge" x="236" y="233" font-size="8">KESTA</text>
    <!-- wheels -->
    <circle cx="215" cy="340" r="55" fill="var(--charcoal)"/>
    <circle cx="215" cy="340" r="47" fill="var(--tire)"/>
    <circle cx="215" cy="340" r="26" fill="#b6b9bd"/>
    <circle cx="815" cy="345" r="55" fill="var(--charcoal)"/>
    <circle cx="815" cy="345" r="47" fill="var(--tire)"/>
    <circle cx="815" cy="345" r="26" fill="#b6b9bd"/>
    <rect x="1132" y="190" width="10" height="80" rx="3" fill="var(--taillight)"/>

    <!-- brand -->
    <rect x="420" y="140" width="40" height="40" fill="var(--brand-orange)"/>
    <text class="brand-name" x="472" y="162" font-size="25">BRIGHTFOLD</text>
    <text class="brand-sub" x="474" y="179" font-size="11">PANEL WORKS</text>

    <!-- services -->
    <g class="service movable-walls">
      <path class="icon-line" d="M422 256 L432 252 L442 256 L452 252 L452 282 L442 286 L432 282 L422 286 Z M432 252 V282 M442 256 V286"/>
      <text class="service-label" x="437" y="301" text-anchor="middle">MOVABLE</text>
      <text class="service-label" x="437" y="312" text-anchor="middle">WALLS</text>
    </g>
    <line x1="478" y1="258" x2="478" y2="305" stroke="#ffffff" stroke-opacity=".6"/>
    <g class="service folding-partitions">
      <path class="icon-line" d="M503 255 L509 259 L515 255 L521 259 L527 255 L533 259 V284 L527 280 L521 284 L515 280 L509 284 L503 280 Z M509 259 V284 M515 255 V280 M521 259 V284 M527 255 V280"/>
      <text class="service-label" x="518" y="301" text-anchor="middle">FOLDING</text>
      <text class="service-label" x="518" y="312" text-anchor="middle">PARTITIONS</text>
    </g>
    <line x1="558" y1="258" x2="558" y2="305" stroke="#ffffff" stroke-opacity=".6"/>
    <g class="service flexible-spaces">
      <path class="icon-line" d="M581 254 H617 V284 H581 Z M581 266 H596 V258 M604 254 V272 H617 M592 284 V274 H604"/>
      <text class="service-label" x="599" y="301" text-anchor="middle">FLEXIBLE</text>
      <text class="service-label" x="599" y="312" text-anchor="middle">SPACES</text>
    </g>
  </g>

  <!-- ===== Rear elevation ===== -->
  <g class="rear-view">
    <path d="M170 418 Q310 406 450 418 Q466 440 468 520 L468 720 L146 720 L148 520 Q150 440 170 418 Z" fill="var(--body-white)" stroke="#d5d8dc"/>
    <g clip-path="url(#rearBody)">
      <rect role="img" aria-label="Photo of a bright meeting room divided by folding partitions" x="146" y="505" width="322" height="125" fill="url(#interiorTone)"/>
      <polygon points="146,590 330,640 468,580 468,720 146,720" fill="var(--navy)"/>
      <polygon points="146,588 330,638 468,578 468,582 330,642 146,592" fill="var(--accent-blue)"/>
    </g>
    <line x1="306" y1="420" x2="306" y2="712" stroke="#8d9196" stroke-width="1"/>
    <rect x="272" y="414" width="70" height="10" rx="4" fill="var(--charcoal)"/>
    <rect x="145" y="555" width="20" height="95" rx="4" fill="var(--taillight)"/>
    <rect x="449" y="555" width="20" height="95" rx="4" fill="var(--taillight)"/>
    <rect x="140" y="715" width="334" height="20" rx="3" fill="var(--charcoal)"/>
    <rect x="152" y="735" width="44" height="38" rx="8" fill="var(--tire)"/>
    <rect x="418" y="735" width="44" height="38" rx="8" fill="var(--tire)"/>

    <rect x="222" y="470" width="30" height="30" fill="var(--brand-orange)"/>
    <text class="brand-name" x="262" y="487" font-size="17">BRIGHTFOLD</text>
    <text class="brand-sub" x="263" y="499" font-size="8">PANEL WORKS</text>

    <g class="contact-block">
      <path d="M186 641 a4 4 0 1 1 8 0 q0 4 -4 8 q-4 -4 -4 -8 Z" fill="var(--label)"/>
      <text class="contact-line" x="198" y="651">218 Lantern Row,</text>
      <text class="contact-line" x="198" y="663">Millbrook NJ 07000</text>
      <path d="M186 675 l3 -1 l2 3 l-1.5 1.5 q1.5 3 4 4 l1.5 -1.5 l3 2 l-1 3 q-8 -1 -11 -11 Z" fill="var(--label)"/>
      <text class="contact-line" x="198" y="682">555-014-0274</text>
      <circle cx="190" cy="695" r="4" fill="none" stroke="var(--label)" stroke-width="1"/>
      <text class="contact-line" x="198" y="698">brightfoldpanels.example</text>
    </g>
  </g>

  <!-- ===== Front elevation ===== -->
  <g class="front-view">
    <path d="M660 425 Q790 410 920 425 Q945 440 958 560 L965 740 L615 740 L622 560 Q635 440 660 425 Z" fill="var(--body-white)" stroke="#d5d8dc"/>
    <path d="M655 445 Q790 435 925 445 Q935 480 937 540 Q790 555 643 540 Q645 480 655 445 Z" fill="var(--glass)"/>
    <rect x="597" y="506" width="30" height="58" rx="8" fill="var(--charcoal)"/>
    <rect x="953" y="506" width="30" height="58" rx="8" fill="var(--charcoal)"/>
    <path d="M630 570 L690 578 L692 600 L632 596 Z" fill="#c9ccd0"/>
    <path d="M950 570 L890 578 L888 600 L948 596 Z" fill="#c9ccd0"/>
    <path d="M640 602 Q790 620 940 602" fill="none" stroke="var(--accent-blue)" stroke-width="3"/>
    <path d="M614 606 Q790 628 966 606 L966 740 L614 740 Z" fill="var(--charcoal)"/>
    <rect x="697" y="620" width="186" height="50" rx="10" fill="var(--tire)"/>
    <text class="maker-badge" x="790" y="651" font-size="14" text-anchor="middle">KESTA</text>
    <rect x="706" y="675" width="168" height="10" rx="3" fill="var(--tire)"/>
    <circle cx="644" cy="714" r="6" fill="#b6b9bd"/>
    <circle cx="936" cy="714" r="6" fill="#b6b9bd"/>
    <rect x="618" y="738" width="44" height="30" rx="8" fill="var(--tire)"/>
    <rect x="918" y="738" width="44" height="30" rx="8" fill="var(--tire)"/>

    <rect x="708" y="572" width="26" height="26" fill="var(--brand-orange)"/>
    <text class="brand-name" x="742" y="586" font-size="14">BRIGHTFOLD</text>
    <text class="brand-sub" x="743" y="596" font-size="7">PANEL WORKS</text>
  </g>
</svg>
</body>
</html>
```